WTF!!! We need a modern professional website for a business litigation law firm.

We need a modern, clean, professional and uncomplicated website for a new business trial and litigation law firm called "Hallorand Trial Firm PLLC". Website must be mobile optimized for iPad and smartphone. The law firm specializes in counseling and representing large corporations, small businesses and entrepreneurs in and out of the courtroom. Lawyers in the firm serve as Florida counsel and trial counsel to organizations facing claims involving product liability, premises liability, professional liability, vehicle and transportation liability, warranty claims, construction defects and delay claims, complex business disputes, commercial litigation and bid disputes in State and Federal Courts. The website is mainly to provide information about the firm, and should include sections describing the firm, identifying the Industries Served and Areas of Practice ," a separate page identifying the "Professionals", a separate page for "Resources & Advisories," and a traveling "Connect With Us" button a site visitor can click on that will launch an email to the Firm's general email account. The website should allow us to easily modify the content on these pages, and let us add/modify links to external information sources. We will not sell anything or take payments through the website. We do need to be able to easily upload and update photographs of attorneys and add new attorneys names/email hyperlinks as the firm grows. We would like to add developments in the law or success stories easily and quickly, such as through a blog page. On the "Connect With Us" page the website should have hyperlinks to email the Firm, and there should be hyperlinks to email each professional on the "Professionals" page. The website should be viewable on mobile devices without distortion. The law firm focuses on trial work and should have some imagery associated with courtrooms, but the overall theme of the site should be modern, clean, and communicate sophistication and strength. The website should be made in Wordpress. We have uploaded logo files for Hallorand Trial Firm.

Target Market(s)

Corporations and companies that are looking for legal representation. Other attorneys/legal industry.

Industry/Entity Type

Legal Industry

Coding

Coded - Design and coding required

Number of Pages Required

1 page

Font styles to use
Sans Serif

Requirements
Must have
• Simple, clean, sophisticated, modern website that includes the logo, watermark of logo, and the elements described above.
Nice to have
• Pictures of city scape, buildings, courtroom, team members.

```html
<!DOCTYPE html>
<html lang="en">
<head>
<meta charset="utf-8">
<title>Hallorand Trial Firm PLLC</title>
<link rel="stylesheet" href="https://fonts.googleapis.com/css2?family=Poppins:wght@300;400;500;600;700;800&display=swap">
<style>
:root{
  --crimson:#9b0a35;
  --crimson-dark:#7d0629;
  --navy:#3d4559;
  --navy-dark:#333a4c;
  --gold:#c9a227;
  --ink:#2b2b2b;
  --text:#444;
  --muted:#8d93a3;
  --paper:#f1f1f1;
  --white:#fff;
}
*{margin:0;padding:0;box-sizing:border-box}
html,body{width:1200px;height:3928px;overflow:hidden}
body{position:relative;font-family:"Poppins",sans-serif;color:var(--text);background:var(--white)}
.abs{position:absolute}
.btn{position:absolute;display:flex;align-items:center;justify-content:center;font-size:12px;font-weight:500;color:var(--white);background:var(--crimson);text-transform:uppercase;letter-spacing:.2px}
.btn.dark{background:var(--navy-dark)}
.heading{font-weight:300;text-transform:uppercase;color:var(--ink);font-size:32px;line-height:1.2;white-space:nowrap}
.heading b{font-weight:700}
.eyebrow{font-size:13px;text-transform:uppercase;color:var(--text)}

/* header */
.site-header{left:0;top:0;width:1200px;height:97px;background:#f5f5f5}
.brand{left:80px;top:30px;font-weight:700;font-size:17px;color:var(--ink);display:flex;align-items:center;gap:8px}
.brand i{display:block;width:12px;height:12px;background:var(--crimson)}
.brand small{display:block;font-size:8px;letter-spacing:3px;font-weight:600}
.nav{left:380px;top:43px;display:flex;gap:21px;font-size:12px;text-transform:uppercase;color:#555}
.nav .active{color:var(--crimson);font-weight:600;position:relative}
.nav .active:after{content:"";position:absolute;left:0;right:0;top:49px;height:3px;background:var(--crimson)}

/* hero */
.hero{left:0;top:97px;width:1200px;height:659px;background:radial-gradient(circle at 38% 35%,#f4e2bd 0,#c9a06a 22%,#7b5230 48%,#4a2f1f 72%,#6d1a1f 100%)}
.hero-title{left:0;width:1200px;top:320px;text-align:center;color:var(--white);font-weight:800;font-size:86px;line-height:1}
.hero-sub{left:0;width:1200px;top:398px;text-align:center;color:var(--white);font-weight:300;font-size:50px;line-height:1}
.hero-tag{left:0;width:1200px;top:452px;text-align:center;color:var(--white);font-size:15px}

/* about */
.about-red{left:0;top:756px;width:455px;height:414px;background:var(--crimson)}
.about-line{left:455px;top:758px;width:745px;height:4px;background:var(--gold)}
.photo-main{left:230px;top:856px;width:348px;height:356px;border:4px solid var(--white);background:linear-gradient(135deg,#2b3550,#7a7f8c 55%,#d9d3c6)}
.photo-small{left:108px;top:1038px;width:219px;height:259px;border:4px solid var(--navy);background:linear-gradient(160deg,#d7c2a4,#6b4527 55%,#2d1d13)}
.award{left:115px;top:936px;color:var(--white);font-size:14px;font-weight:600;line-height:1.2}
.case{left:350px;top:1230px;display:flex;align-items:center;gap:10px;font-size:14px;font-weight:600;color:var(--ink)}
.about-copy{left:606px;top:872px;width:470px}
.about-copy .heading{margin-top:14px}
.about-copy p{font-size:12.5px;line-height:23px;margin-top:20px;color:#333}
.watermark{left:835px;top:1100px;width:340px;height:285px;background:radial-gradient(ellipse at center,#f6f0f1 0,#fff 70%)}

/* practice */
.practice{left:0;top:1385px;width:1200px;height:715px;background:var(--paper)}
.card{position:absolute;width:245px;color:var(--white)}
.card span{position:absolute;left:18px;bottom:30px;font-size:17px;font-weight:300;text-transform:uppercase;line-height:23px}
.card span b{font-weight:600}
.card.raised{box-shadow:0 18px 30px rgba(0,0,0,.18)}
.dots{left:80px;top:2033px;display:flex;gap:12px}
.dots i{width:8px;height:8px;border-radius:50%;background:#c4c4c4}
.dots i:first-child{background:var(--crimson)}
.arrow{position:absolute;width:50px;height:49px;display:flex;align-items:center;justify-content:center}

/* director */
.dir-band{left:0;top:2450px;width:428px;height:200px;background:var(--crimson)}
.dir-box{left:428px;top:2243px;width:649px;height:407px;background:linear-gradient(100deg,var(--crimson),#a51a44)}
.dir-photo{left:139px;top:2137px;width:280px;height:330px;border:4px solid var(--navy);background:linear-gradient(180deg,#e8e8e8,#9a9a9a 60%,#2a2a2a)}
.dir-name{left:139px;width:280px;top:2478px;text-align:center;color:var(--white);font-size:24px;font-weight:300;white-space:nowrap}
.dir-name b{font-weight:700}
.dir-role{left:139px;width:280px;top:2536px;text-align:center;color:var(--white);font-size:14px;line-height:22px}
.dir-head{left:462px;top:2285px;color:var(--white);font-size:33px;font-weight:300;line-height:42px}
.dir-head b{font-weight:700}
.dir-copy{left:468px;top:2393px;width:540px;color:var(--white);font-size:14.5px;line-height:22.5px}

/* industries */
.ind-head{left:0;width:1200px;top:2750px;text-align:center}
.ind-sub{left:0;width:1200px;top:2815px;text-align:center;font-size:13px;color:#333}
.chip{position:absolute;height:78px;background:var(--navy);color:var(--white);display:flex;align-items:center;gap:14px;padding-left:14px;font-size:17px;font-weight:300;text-transform:uppercase;white-space:nowrap}
.chip b{font-weight:700}
.chip svg{flex:none}

/* connect + footer */
.foot-bg{left:0;top:3420px;width:1200px;height:508px;background:var(--navy)}
.foot-line{left:0;top:3403px;width:1200px;height:3px;background:var(--navy)}
.connect-box{left:113px;top:3323px;width:973px;height:192px;background:linear-gradient(100deg,var(--crimson),#a8173f)}
.scales{left:120px;top:3268px;width:180px;height:242px;background:linear-gradient(180deg,#d9c6a0,#8a6a43 60%,#c9b99a)}
.connect-title{left:333px;top:3355px;color:var(--white);font-size:42px;font-weight:300;text-transform:uppercase;line-height:1.2;white-space:nowrap}
.connect-title b{font-weight:700}
.connect-copy{left:333px;top:3423px;color:var(--white);font-size:13px;line-height:23px}
.f-col{position:absolute;top:3568px;color:#aeb3c1;font-size:13px}
.f-col h4{color:var(--white);font-size:17px;font-weight:300;text-transform:uppercase;margin-bottom:22px}
.f-col h4 b{font-weight:600}
.f-col li{list-style:none;margin-bottom:9px;line-height:20px}
.f-label{color:var(--white);font-weight:600;display:flex;align-items:center;gap:8px;margin-bottom:6px}
.f-col .val{margin-bottom:14px}
.f-brand{left:113px;top:3612px;width:170px;color:var(--white);text-align:center;font-weight:700;font-size:26px;line-height:1}
.f-brand small{display:block;font-size:12px;letter-spacing:5px;font-weight:500;margin-top:6px}
.social{left:160px;top:3730px;display:flex;gap:18px}
.social i{width:18px;height:18px;border-radius:50%;background:var(--white);display:block}
.copy-line{left:113px;top:3852px;width:973px;height:1px;background:#6a7184}
.copyright{left:0;width:1200px;top:3882px;text-align:center;color:var(--white);font-size:13px}
</style>
</head>
<body>

<header class="abs site-header">
  <div class="abs brand"><i></i><div>HALLORAND<small>TRIAL FIRM</small></div></div>
  <nav class="abs nav">
    <span class="active">Home</span><span>Areas of Practice</span><span>Industries Served</span><span>Professionals</span><span>Resources &amp; Advisories</span>
  </nav>
  <div class="btn" style="left:1022px;top:28px;width:125px;height:42px">Contact Us</div>
</header>

<section class="abs hero" role="img" aria-label="Bronze statue of Lady Justice before law books in warm light"></section>
<div class="abs hero-title">HALLORAND</div>
<div class="abs hero-sub">TRIAL FIRM PLLC</div>
<div class="abs hero-tag">When success matters most, you can count on us.</div>
<div class="btn" style="left:537px;top:500px;width:124px;height:41px">Read More</div>

<!-- about -->
<div class="abs watermark"></div>
<div class="abs about-red"></div>
<div class="abs about-line"></div>
<div class="abs photo-main" role="img" aria-label="Attorney signing documents at a desk"></div>
<div class="abs photo-small" role="img" aria-label="Justice statue, open book and gavel"></div>
<div class="abs award">
  <svg width="34" height="42" viewBox="0 0 34 42" fill="none" stroke="#fff" stroke-width="2"><circle cx="17" cy="15" r="12"/><circle cx="17" cy="15" r="7"/><path d="M9 25l-3 14 11-6 11 6-3-14"/></svg>
  <div style="margin-top:6px">Global<br>Award win</div>
</div>
<div class="abs case">
  <svg width="44" height="40" viewBox="0 0 44 40" fill="none" stroke="#3d4559" stroke-width="2"><path d="M3 12L22 2l19 10H3z"/><path d="M8 14v18M16 14v18M28 14v18M36 14v18M3 34h38M1 38h42"/></svg>
  Case Solved
</div>
<div class="abs about-copy">
  <div class="eyebrow">About Us</div>
  <div class="heading">Your Defense, <b>Our Mission</b></div>
  <p>The Hallorand Trial Firm PLLC, headquartered in the heart of New York City, is a boutique litigation firm specializing in representing corporations, small businesses, and entrepreneurs in both State and Federal Courts. With a reputation for delivering exceptional and innovative legal representation, we are dedicated to handling our clients' most sensitive and significant legal matters with sophistication and strength.</p>
</div>
<div class="btn" style="left:606px;top:1161px;width:124px;height:42px">Read More</div>

<!-- practice -->
<section class="abs practice"></section>
<svg class="abs" style="left:0;top:1385px" width="110" height="100" viewBox="0 0 110 100" fill="none" stroke="#b8bcc6" stroke-width="3"><path d="M104 0A104 104 0 0 1 0 98"/><path d="M92 0A92 92 0 0 1 0 86"/><path d="M80 0A80 80 0 0 1 0 74"/><path d="M68 0A68 68 0 0 1 0 62"/></svg>
<div class="abs eyebrow" style="left:0;width:1200px;top:1447px;text-align:center">Our Expertise</div>
<div class="abs heading" style="left:0;width:1200px;top:1467px;text-align:center">Our Practice <b>Areas</b></div>

<div class="card" style="left:74px;top:1584px;height:371px;background:linear-gradient(180deg,#cdbb9d,#8a7a63 60%,#4d4a52)" role="img" aria-label="Lawyer addressing a judge in court"><span>Litigation &amp;<br>Government<br><b>Enforcement</b></span></div>
<div class="card raised" style="left:345px;top:1568px;height:403px;background:linear-gradient(180deg,#5b4d66,#2c3258 45%,#3d4559)" role="img" aria-label="Gavel and hands writing notes"><span>Internal<br><b>Investigations</b></span></div>
<div class="card" style="left:615px;top:1584px;height:371px;background:linear-gradient(180deg,#b9c8d4,#8494a6 55%,#4c5568)" role="img" aria-label="Advisor taking notes with a client"><span>Crisis<br><b>Counseling</b></span></div>
<div class="card raised" style="left:886px;top:1568px;height:403px;background:linear-gradient(180deg,#3a4a6a,#8a6d4f 55%,#5a4a44)" role="img" aria-label="Lawyers reviewing papers beside a gavel"><span>Legal &amp;<br>Litigation<br><b>Management</b></span></div>
<div class="arrow" style="left:526px;top:1545px;width:44px;height:57px;background:var(--crimson)"><svg width="10" height="14" viewBox="0 0 10 14" fill="none" stroke="#fff" stroke-width="2"><path d="M2 1l6 6-6 6"/></svg></div>
<div class="abs dots"><i></i><i></i><i></i></div>
<div class="arrow" style="left:1005px;top:2000px;background:#c9ccd3"><svg width="22" height="12" viewBox="0 0 22 12" fill="none" stroke="#fff" stroke-width="2"><path d="M21 6H2M7 1L2 6l5 5"/></svg></div>
<div class="arrow" style="left:1081px;top:2000px;background:var(--crimson)"><svg width="22" height="12" viewBox="0 0 22 12" fill="none" stroke="#fff" stroke-width="2"><path d="M1 6h19M15 1l5 5-5 5"/></svg></div>

<!-- director -->
<div class="abs" style="left:0;top:2448px;width:139px;height:4px;background:var(--gold)"></div>
<div class="abs dir-band"></div>
<div class="abs dir-box"></div>
<div class="abs" style="left:1035px;top:2240px;width:165px;height:3px;background:var(--navy)"></div>
<div class="abs" style="left:139px;top:2652px;width:942px;height:4px;background:var(--navy)"></div>
<div class="abs" style="left:0;top:2654px;width:120px;height:3px;background:var(--navy)"></div>
<div class="abs" style="left:1074px;top:2467px;width:4px;height:189px;background:var(--navy)"></div>
<svg class="abs" style="left:1078px;top:2467px" width="122" height="105" viewBox="0 0 122 105" fill="none" stroke="#b8bcc6" stroke-width="3"><path d="M10 0A112 112 0 0 0 122 100"/><path d="M22 0A100 100 0 0 0 122 88"/><path d="M34 0A88 88 0 0 0 122 76"/><path d="M46 0A76 76 0 0 0 122 64"/></svg>
<div class="abs dir-photo" role="img" aria-label="Portrait of the firm's founder"></div>
<div class="abs dir-name">MARCUS T. <b>HALLORAND</b></div>
<div class="abs dir-role">founder of The Hallorand<br>Law Firm</div>
<div class="abs dir-head">GUIDING PRINCIPLES FROM<br><b>OUR DIRECTOR</b></div>
<div class="abs dir-copy">With three decades of legal excellence, Marcus T. Hallorand, the founder of The Hallorand Trial Firm PLLC, brings unparalleled expertise to the firm. A graduate in the top 1% of his class from Ashbury Law School, Mr. Hallorand has dedicated his career to representing individual and corporate clients through all phases of sophisticated criminal and civil litigation.</div>
<div class="btn dark" style="left:470px;top:2563px;width:122px;height:41px">Read More</div>

<!-- industries -->
<div class="abs heading ind-head">Industries We <b>Serve</b></div>
<div class="abs ind-sub">Hallorand Trial Firm PLLC provides legal expertise tailored to industries and organizations facing</div>

<div class="chip" style="left:179px;top:2865px;width:254px"><svg width="40" height="40" viewBox="0 0 40 40" fill="none" stroke="#fff" stroke-width="1.6"><rect x="12" y="4" width="20" height="24"/><path d="M16 11h12M16 16h12M16 21h8M4 30l8-4 8 6 10-4 6 4"/></svg><span>Product <b>Liability</b></span></div>
<div class="chip" style="left:449px;top:2865px;width:254px"><svg width="40" height="40" viewBox="0 0 40 40" fill="none" stroke="#fff" stroke-width="1.6"><rect x="12" y="4" width="22" height="28"/><path d="M16 10h14M16 15h14M16 20h10M4 24h10v12H4z"/></svg><span>Premises <b>Liability</b></span></div>
<div class="chip" style="left:719px;top:2865px;width:302px"><svg width="40" height="40" viewBox="0 0 40 40" fill="none" stroke="#fff" stroke-width="1.6"><rect x="5" y="12" width="30" height="20" rx="2"/><path d="M15 12V8h10v4M5 20h30"/><circle cx="13" cy="27" r="5"/></svg><span>Professional <b>Liability</b></span></div>

<div class="chip" style="left:122px;top:2961px;width:459px;padding-left:22px;gap:18px"><svg width="40" height="40" viewBox="0 0 40 40" fill="none" stroke="#fff" stroke-width="1.6"><circle cx="20" cy="20" r="16" stroke-dasharray="3 3"/><rect x="11" y="12" width="18" height="16" rx="3"/><path d="M11 20h18"/><circle cx="15" cy="24" r="1.5"/><circle cx="25" cy="24" r="1.5"/></svg><span>Vehicle and Transportation <b>Liability</b></span></div>
<div class="chip" style="left:605px;top:2961px;width:472px;padding-left:18px"><svg width="40" height="40" viewBox="0 0 40 40" fill="none" stroke="#fff" stroke-width="1.6"><path d="M20 4v30M8 10h24M8 10l-5 12h10zM32 10l-5 12h10zM12 34h16"/></svg><span>Construction Defects &amp; <b>Delay Claims</b></span></div>

<div class="chip" style="left:142px;top:3057px;width:358px;padding-left:20px"><svg width="40" height="40" viewBox="0 0 40 40" fill="none" stroke="#fff" stroke-width="1.6"><circle cx="20" cy="8" r="4"/><circle cx="9" cy="22" r="4"/><circle cx="31" cy="22" r="4"/><path d="M14 18h12M3 34c0-4 3-7 6-7s6 3 6 7M25 34c0-4 3-7 6-7s6 3 6 7"/></svg><span>Complex Business <b>Disputes</b></span></div>
<div class="chip" style="left:517px;top:3057px;width:330px;padding-left:20px"><svg width="40" height="40" viewBox="0 0 40 40" fill="none" stroke="#fff" stroke-width="1.6"><rect x="4" y="6" width="14" height="28"/><path d="M8 12h6M8 18h6M8 24h6"/><circle cx="28" cy="24" r="8"/><path d="M28 19v10M23 24h10"/></svg><span>Commercial <b>Litigation</b></span></div>
<div class="chip" style="left:863px;top:3057px;width:222px;padding-left:20px"><svg width="40" height="40" viewBox="0 0 40 40" fill="none" stroke="#fff" stroke-width="1.6"><path d="M20 4v30M6 10h28M6 10l-4 10h8zM34 10l-4 10h8zM12 34h16"/><rect x="15" y="18" width="10" height="10"/></svg><span>Bid <b>Disputes</b></span></div>

<div class="chip" style="left:463px;top:3153px;width:274px;padding-left:20px"><svg width="40" height="40" viewBox="0 0 40 40" fill="none" stroke="#fff" stroke-width="1.6"><path d="M20 3l14 6v10c0 9-6 15-14 18C12 34 6 28 6 19V9z"/><path d="M13 20l5 5 9-10"/></svg><span>Warranty <b>Claims</b></span></div>

<!-- connect -->
<div class="abs foot-line"></div>
<div class="abs foot-bg"></div>
<div class="abs connect-box"></div>
<div class="abs scales" role="img" aria-label="Brass scales of justice on stacked books with a gavel"></div>
<h2 class="abs connect-title">Connect <b>With Us</b></h2>
<div class="abs connect-copy">We value meaningful connections with our clients.<br>Click the "Connect With Us" button to email the firm directly or visit<br>our contact page for further information.</div>
<div class="btn dark" style="left:880px;top:3377px;width:137px;height:41px">Contact Us</div>

<!-- footer -->
<div class="abs f-brand">HALLORAND<small>TRIAL FIRM</small></div>
<div class="abs social" aria-label="Social profiles"><i></i><i></i></div>

<div class="f-col" style="left:368px;width:220px">
  <h4>Contact <b>Info</b></h4>
  <div class="f-label"><svg width="13" height="13" viewBox="0 0 24 24" fill="#fff"><path d="M6.6 10.8a15 15 0 0 0 6.6 6.6l2.2-2.2a1 1 0 0 1 1-.25 11 11 0 0 0 3.6.6 1 1 0 0 1 1 1V20a1 1 0 0 1-1 1A17 17 0 0 1 3 4a1 1 0 0 1 1-1h3.5a1 1 0 0 1 1 1c0 1.25.2 2.45.6 3.6a1 1 0 0 1-.25 1z"/></svg>Phone</div>
  <div class="val">212.555.0148</div>
  <div class="f-label"><svg width="13" height="11" viewBox="0 0 24 18" fill="#fff"><path d="M0 0h24v18H0z"/><path d="M0 0l12 9 12-9" stroke="#3d4559" stroke-width="2" fill="none"/></svg>Email</div>
  <div class="val">info@hallorandlaw.com</div>
  <div class="f-label"><svg width="11" height="14" viewBox="0 0 12 16" fill="none" stroke="#fff" stroke-width="1.6"><path d="M6 15s5-5.5 5-9A5 5 0 0 0 1 6c0 3.5 5 9 5 9z"/><circle cx="6" cy="6" r="2"/></svg>Visit Us</div>
  <div style="font-size:11px;line-height:16px">THE HALLORAND LAW FIRM PLLC<br>410 Carrow Avenue, 12th Floor,<br>New York, NY 10017</div>
</div>
<div class="f-col" style="left:647px">
  <h4><b>Quick Links</b></h4>
  <ul><li>Home</li><li>Industries Served</li><li>Professionals</li><li>Resources &amp; Advisories</li><li>Contact Us</li></ul>
</div>
<div class="f-col" style="left:890px;width:200px">
  <h4>Areas of <b>Practice</b></h4>
  <ul style="padding-left:16px">
    <li style="list-style:disc">Internal Investigations</li>
    <li style="list-style:disc">Crisis Counseling</li>
    <li style="list-style:disc">Legal and Litigation Management</li>
    <li style="list-style:disc">Litigation and Government Enforcement</li>
  </ul>
</div>
<div class="abs copy-line"></div>
<div class="abs copyright">©2024 Copyrights Hallorand Trial Firm. All rights reserved.</div>

</body>
</html>
```